Women's Online Clothing Boutique Needs Business Cards

I already have a logo that I would like to use. Some of the things that interest me is black business cards, foil embossed logo, glossy embossed logo, leopard print, no yellow font, rounded edges. I even like just a large logo on the front side with all of my information on the back side.

Contact Information for Business Card

https://silverheron.shopvenlo.com/
https://www.pagelink.net/thesilverheronboutique/
https://www.picfeed.net/thesilverheronboutique/
silverheronboutique@mailora.net

Requirements
Must have
• My Logo
Nice to have
• Leopard Print
Should not have
• No Yellow Font

```html
<!DOCTYPE html>
<html lang="en">
<head>
<meta charset="utf-8">
<title>The Silver Heron Boutique – Business Cards</title>
<link href="https://fonts.googleapis.com/css2?family=Roboto:wght@400;500;700&display=swap" rel="stylesheet">
<style>
  :root {
    --backdrop: #8c7a66;
    --card-white: #ffffff;
    --gold: #b8862b;
    --gold-light: #d4a437;
    --brown-dark: #2f2a25;
    --text-dark: #3d3329;
    --ink: #5e5e5e;
    --white: #ffffff;
  }
  * { margin: 0; padding: 0; box-sizing: border-box; }
  html, body { width: 900px; height: 1200px; overflow: hidden; }
  body {
    background: var(--backdrop);
    font-family: "Roboto", Arial, sans-serif;
    position: relative;
  }
  .card {
    position: absolute;
    left: 81px;
    width: 740px;
    height: 438px;
    border-radius: 30px;
    overflow: hidden;
    box-shadow: 0 10px 28px rgba(0,0,0,0.35);
  }
  .card-front { top: 126px; background: var(--card-white); }
  .card-back {
    top: 640px;
    background: linear-gradient(90deg, var(--brown-dark) 0%, #5c4a30 45%, var(--gold-light) 100%);
  }
  .brand {
    display: inline-block;
    font-weight: 500;
    letter-spacing: 0.5px;
    line-height: 1.1;
    text-align: center;
  }
  .brand-front {
    position: absolute;
    left: 40px; top: 88px;
    color: var(--text-dark);
    font-size: 38px;
  }
  .brand-front .brand-sub { font-size: 32px; }
  .holder {
    position: absolute;
    right: 60px; top: 60px;
    text-align: right;
  }
  .holder-name { color: var(--text-dark); font-weight: 700; font-size: 24px; }
  .holder-role { color: var(--ink); font-size: 16px; margin-top: 2px; }
  .contacts {
    position: absolute;
    left: 40px; top: 300px;
    list-style: none;
  }
  .contacts li {
    display: flex; align-items: center;
    color: var(--ink);
    font-size: 17px;
    height: 26px;
  }
  .contacts svg { width: 15px; height: 15px; margin-right: 10px; flex: none; }
  .brand-back {
    position: absolute;
    left: 60px; top: 95px;
    color: var(--white);
    font-size: 44px;
  }
  .brand-back .brand-sub { font-size: 38px; }
</style>
</head>
<body>
  <section class="card card-front">
    <div class="brand brand-front">
      <div>The Silver Heron</div>
      <div class="brand-sub">Boutique</div>
    </div>
    <div class="holder">
      <div class="holder-name">Daniel Harper</div>
      <div class="holder-role">Manager</div>
    </div>
    <ul class="contacts">
      <li><svg viewBox="0 0 16 16"><rect x="1" y="1" width="14" height="14" rx="2" fill="var(--gold)"/></svg>thesilverheronboutique</li>
      <li><svg viewBox="0 0 16 16"><rect x="1" y="1" width="14" height="14" rx="2" fill="var(--gold)"/></svg>thesilverheronboutique</li>
      <li><svg viewBox="0 0 16 16"><rect x="1" y="3" width="14" height="10" rx="1.5" fill="none" stroke="var(--gold)" stroke-width="1.6"/><path d="M1.5 4 L8 9 L14.5 4" fill="none" stroke="var(--gold)" stroke-width="1.6"/></svg>silverheronboutique@mailora.net</li>
      <li><svg viewBox="0 0 16 16"><circle cx="8" cy="8" r="6.5" fill="none" stroke="var(--gold)" stroke-width="1.6"/><ellipse cx="8" cy="8" rx="2.8" ry="6.5" fill="none" stroke="var(--gold)" stroke-width="1.2"/><line x1="1.5" y1="8" x2="14.5" y2="8" stroke="var(--gold)" stroke-width="1.2"/></svg>silverheron.shopvenlo.com</li>
    </ul>
  </section>

  <section class="card card-back">
    <div class="brand brand-back">
      <div>The Silver Heron</div>
      <div class="brand-sub">Boutique</div>
    </div>
  </section>
</body>
</html>
```